Business Card Design for Lawn Management

Lawn Management

Industry/Entity Type

Business

Contact Information for Business Card

Calloway Lawn Management
Doran Calloway
Calloway_Lawn@brindlemail.com
404-627-1845

```html
<!DOCTYPE html>
<html lang="en">
<head>
<meta charset="utf-8">
<title>Calloway Lawn Management — Business Card</title>
<link href="https://fonts.googleapis.com/css2?family=Russo+One&family=Roboto:wght@300;400;700&display=swap" rel="stylesheet">
<style>
  :root {
    --page: #e9e6df;
    --leaf: #3fae4a;
    --leaf-dark: #1f7a2c;
    --leaf-deep: #17652a;
    --grass-light: #7cbf3c;
    --grass-dark: #3e7d22;
    --paper: #ffffff;
    --ink-light: #ffffff;
  }
  * { box-sizing: border-box; margin: 0; padding: 0; }
  html, body { width: 1200px; height: 1023px; overflow: hidden; background: var(--page); }
  .sheet { position: relative; width: 1200px; height: 1023px; }

  .card {
    position: absolute; left: 220px; width: 760px; height: 434px;
    overflow: hidden; border-radius: 4px;
    box-shadow: 0 10px 28px rgba(0,0,0,0.22);
  }
  .card--front { top: 52px; background: var(--paper); }
  .card--back  { top: 537px; background: radial-gradient(ellipse at 60% 35%, #4cc75a 0%, var(--leaf) 35%, var(--leaf-deep) 100%); }

  .front-grass { position: absolute; inset: 0; width: 760px; height: 434px; }

  .contact-band {
    position: absolute; top: 0; left: 370px; width: 300px; height: 165px;
    background: rgba(23, 101, 42, 0.55);
    padding: 38px 0 0 26px;
    color: var(--ink-light); font-family: "Roboto", sans-serif;
  }
  .contact-name { font-weight: 700; font-size: 22px; letter-spacing: 0.5px; margin-bottom: 16px; }
  .contact-line { font-weight: 400; font-size: 16px; line-height: 24px; }

  .brand {
    position: absolute; left: 70px; top: 250px;
    display: flex; align-items: center; gap: 26px;
  }
  .brand-dot { width: 110px; height: 110px; border-radius: 50%; background: var(--leaf); flex: none; }
  .brand-name {
    font-family: "Russo One", sans-serif; color: var(--leaf);
    font-size: 58px; line-height: 1; letter-spacing: 1px; text-transform: uppercase;
  }
  .brand-sub {
    font-family: "Roboto", sans-serif; font-weight: 300; color: var(--leaf);
    font-size: 28px; margin-top: 4px;
  }

  .back-title { position: absolute; left: 44px; top: 40px; color: var(--ink-light); }
  .back-title .brand-name { color: var(--ink-light); font-size: 54px; }
  .back-title .brand-sub { color: var(--ink-light); font-size: 26px; }

  .back-mark {
    position: absolute; left: 420px; top: 90px; width: 290px; height: 290px; border-radius: 50%;
    background: radial-gradient(circle at 40% 40%, var(--grass-light), var(--grass-dark));
  }
</style>
</head>
<body>
<main class="sheet">

  <section class="card card--front" aria-label="Business card front">
    <svg class="front-grass" viewBox="0 0 760 434" role="img" aria-label="Close-up photograph of green lawn grass">
      <defs>
        <linearGradient id="grassTone" x1="0" y1="0" x2="1" y2="1">
          <stop offset="0" stop-color="#6fb236"/>
          <stop offset="0.5" stop-color="#4f9a2a"/>
          <stop offset="1" stop-color="#2f6e1f"/>
        </linearGradient>
      </defs>
      <path d="M0 0 H760 V150 C560 170 420 140 330 170 C240 200 120 210 0 200 Z" fill="url(#grassTone)"/>
    </svg>

    <div class="contact-band">
      <p class="contact-name">Doran Calloway</p>
      <p class="contact-line">404-627-1845</p>
      <p class="contact-line">Calloway_Lawn@brindlemail.com</p>
    </div>

    <div class="brand">
      <span class="brand-dot" aria-hidden="true"></span>
      <div>
        <p class="brand-name">Calloway</p>
        <p class="brand-sub">Lawn Management</p>
      </div>
    </div>
  </section>

  <section class="card card--back" aria-label="Business card back">
    <div class="back-title">
      <p class="brand-name">Calloway</p>
      <p class="brand-sub">Lawn Management</p>
    </div>
    <div class="back-mark" role="img" aria-label="Large circle filled with a photograph of lawn grass"></div>
  </section>

</main>
</body>
</html>
```